Business Card Design Project

Looking for a business card that our customers will remember. We are a high end Travel Agency.
Need a re-memorable classy business card.
Both sides full color.
Must have the following details.
Voyage Harbor Logo (see attached)
4B Wattle Lane
Penhurst Sydney NSW 2241
Phone: 02 9471 3652
Fax: 02 9563 4417
sales@voyageharbor-example.com.au
Consultant Name
Anything else you think we need

```html
<!DOCTYPE html>
<html lang="en">
<head>
<meta charset="utf-8">
<title>Voyage Harbor – Business Card</title>
<link href="https://fonts.googleapis.com/css2?family=Ubuntu:wght@400;500;700&display=swap" rel="stylesheet">
<style>
  :root {
    --page-bg: #2a2a2c;
    --navy: #22395c;
    --navy-deep: #182a45;
    --navy-soft: #2d4a74;
    --silver: #e4e6ea;
    --silver-dark: #b9bec6;
    --white: #ffffff;
    --accent: #e1b12c;
    --logo-ink: #1f3a5f;
  }
  * { box-sizing: border-box; margin: 0; padding: 0; }
  html, body { width: 1200px; height: 900px; overflow: hidden; }
  body {
    background: var(--page-bg);
    font-family: "Ubuntu", Arial, sans-serif;
    position: relative;
  }
  .card {
    position: absolute;
    width: 600px;
    height: 343px;
    overflow: hidden;
    box-shadow: 0 14px 30px rgba(0,0,0,.45);
  }

  /* Back side */
  .card-back {
    left: 80px; top: 80px;
    background: linear-gradient(135deg, var(--navy-soft), var(--navy) 55%, var(--navy-deep));
  }
  .world-map {
    position: absolute;
    left: 40px; top: 24px; width: 520px; height: 250px;
    border-radius: 40px;
    background: radial-gradient(ellipse at center, rgba(120,145,185,.35), rgba(120,145,185,0) 70%);
  }
  .back-logo-band {
    position: absolute;
    left: 0; top: 150px; width: 330px; height: 64px;
    background: linear-gradient(180deg, var(--white), var(--silver));
    display: flex; align-items: center; padding-left: 34px; gap: 12px;
  }
  .back-web {
    position: absolute; right: 34px; bottom: 26px;
    color: var(--white); font-size: 14px; letter-spacing: .3px;
  }

  /* Logo lockup */
  .brand-mark {
    width: 14px; height: 14px; border-radius: 50%;
    background: var(--accent);
    flex: none;
  }
  .brand-name {
    font-family: "Ubuntu", Arial, sans-serif;
    font-weight: 700;
    color: var(--logo-ink);
    font-size: 28px;
    letter-spacing: .5px;
    white-space: nowrap;
  }

  /* Front side */
  .card-front {
    left: 520px; top: 470px;
    background: var(--white);
  }
  .stripe { position: absolute; left: 0; width: 100%; }
  .stripe-top-1 { top: 10px; height: 7px; background: var(--navy); }
  .stripe-top-2 { top: 23px; height: 5px; background: var(--navy); }
  .front-upper {
    position: absolute; top: 34px; left: 0; width: 100%; height: 110px;
    background: linear-gradient(90deg, var(--navy-deep), var(--navy) 60%, var(--navy-soft));
  }
  .dot-field {
    position: absolute; right: 0; top: 0; width: 300px; height: 110px;
    background: linear-gradient(90deg, rgba(140,165,200,0), rgba(140,165,200,.28));
  }
  .consultant {
    position: absolute; left: 44px; top: 58px; color: var(--white);
  }
  .consultant-name { font-size: 24px; font-weight: 700; line-height: 1.1; }
  .consultant-role { font-size: 18px; font-weight: 400; margin-top: 4px; }
  .front-band {
    position: absolute; top: 144px; left: 0; width: 100%; height: 60px;
    background: linear-gradient(180deg, var(--white), var(--silver) 60%, var(--silver-dark));
    display: flex; align-items: center; justify-content: flex-end;
    padding-right: 40px; gap: 12px;
  }
  .front-lower {
    position: absolute; top: 204px; left: 0; width: 100%; height: 96px;
    background: linear-gradient(90deg, var(--navy-deep), var(--navy));
    color: var(--white);
    font-size: 15px;
    display: flex; gap: 44px;
    padding: 16px 0 0 44px;
  }
  .contact-list { list-style: none; display: flex; flex-direction: column; gap: 14px; }
  .contact-list li { display: flex; align-items: flex-start; gap: 12px; line-height: 1.2; }
  .contact-list svg { flex: none; width: 18px; height: 18px; fill: var(--white); }
  .stripe-bottom-1 { top: 306px; height: 5px; background: var(--navy); }
  .stripe-bottom-2 { top: 317px; height: 7px; background: var(--navy); }
</style>
</head>
<body>

  <section class="card card-back" aria-label="Business card, back">
    <div class="world-map" role="img" aria-label="Faint world map in the background"></div>
    <div class="back-logo-band">
      <span class="brand-mark"></span>
      <span class="brand-name">Voyage Harbor</span>
    </div>
    <p class="back-web">www.voyageharbor-example.com.au</p>
  </section>

  <section class="card card-front" aria-label="Business card, front">
    <div class="stripe stripe-top-1"></div>
    <div class="stripe stripe-top-2"></div>
    <div class="front-upper">
      <div class="dot-field" role="img" aria-label="Decorative field of soft dots"></div>
    </div>
    <div class="consultant">
      <p class="consultant-name">Liam Carter</p>
      <p class="consultant-role">Consultant</p>
    </div>
    <div class="front-band">
      <span class="brand-mark"></span>
      <span class="brand-name">Voyage Harbor</span>
    </div>
    <div class="front-lower">
      <ul class="contact-list">
        <li>
          <svg viewBox="0 0 18 18" aria-hidden="true"><path d="M5 1h8a1 1 0 0 1 1 1v14a1 1 0 0 1-1 1H5a1 1 0 0 1-1-1V2a1 1 0 0 1 1-1zm1 2v10h6V3zm3 11a1 1 0 1 0 0 2 1 1 0 0 0 0-2z"/></svg>
          <span>02 9471 3652</span>
        </li>
        <li>
          <svg viewBox="0 0 18 18" aria-hidden="true"><path d="M5 1h8v5H5zM2 7h14a1 1 0 0 1 1 1v6h-3v3H4v-3H1V8a1 1 0 0 1 1-1zm4 6v2h6v-2z"/></svg>
          <span>02 9563 4417</span>
        </li>
      </ul>
      <ul class="contact-list">
        <li>
          <svg viewBox="0 0 18 18" aria-hidden="true"><path d="M1 4h16v10H1zm1.5 1.2L9 10l6.5-4.8V5H2.5z"/></svg>
          <span>sales@voyageharbor-example.com.au</span>
        </li>
        <li>
          <svg viewBox="0 0 18 18" aria-hidden="true"><path d="M9 1a6 6 0 0 1 6 6c0 4.5-6 10-6 10S3 11.5 3 7a6 6 0 0 1 6-6zm0 3.5a2.5 2.5 0 1 0 0 5 2.5 2.5 0 0 0 0-5z"/></svg>
          <span>4B Wattle Lane<br>Penhurst Sydney NSW 2241</span>
        </li>
      </ul>
    </div>
    <div class="stripe stripe-bottom-1"></div>
    <div class="stripe stripe-bottom-2"></div>
  </section>

</body>
</html>
```